International Life Insurer Needs a Web Design

What We Do: We are a boutique financial services firm specializing in solutions that financial services professionals can integrate into comprehensive wealth preservation strategies for their clients. Strategies we provide may run the spectrum from simple life insurance products to complex cases with very sophisticated and intricate solutions.

Industry Type: Financial & Insurance

Top Things to Communicate Through Our Web Design:
#1 Ultra High Net Worth
#2 INTERNATIONAL
#3 Private Banking
#4 Expertise
________________________________________
Our Target Audience:
Financial institutions/private banks who have high net worth/ultra high net worth international clients looking for unparalleled expertise in wealth preservation, taxation, and business insurance. The audience is the financial service professional, not the end client of the financial services. We will direct the professional to the site.
We Like These Designs. (fonts, colors, style):
Simple font, clean, modern, contemporary, blue colors
NOT stodgy, old, gothic, etc.

Secondarily, we’d like to also create a small tri-fold brochure incorporating the web elements (design, text), so the ability to transfer the design to print might be a plus.

Project Deadline Extended
Reason: to allow for additional design work

Target Market(s)

Financial services professionals catering to their ultra high net worth clients

Industry/Entity Type

Life Insurance

Requirements
Must have
• Our logo (see uploaded file)
Nice to have
• the existing website includes some text that could be reviewed for ideas and incorporated into the design: http://marlowcrestadvisory.example/

```html
<!DOCTYPE html>
<html lang="en">
<head>
<meta charset="utf-8">
<title>Marlowcrest Advisory Group</title>
<link href="https://fonts.googleapis.com/css2?family=Inter:wght@300;400;500&display=swap" rel="stylesheet">
<style>
  :root {
    --white: #ffffff;
    --navy: #003a78;
    --navy-deep: #00295a;
    --brand-blue: #0a4f9c;
    --tab-blue: #0066b8;
    --panel-blue: #006bbd;
    --gap-blue: #00508f;
    --photo-light: #eef1f4;
    --photo-mid: #c9d3de;
  }
  * { margin: 0; padding: 0; box-sizing: border-box; }
  html, body { width: 1200px; height: 960px; overflow: hidden; }
  body {
    font-family: "Inter", "Helvetica Neue", Arial, sans-serif;
    background: var(--navy-deep);
    position: relative;
  }
  .site-header {
    position: absolute; left: 0; top: 0; width: 1200px; height: 300px;
    background: var(--white);
  }
  .brand {
    position: absolute; left: 43px; top: 35px;
    display: flex; align-items: center; gap: 14px;
  }
  .brand-square { width: 100px; height: 98px; background: var(--brand-blue); }
  .brand-name {
    font-size: 38px; font-weight: 400; line-height: 36px;
    color: var(--brand-blue); letter-spacing: -0.5px;
  }
  .hero-photo {
    position: absolute; left: 570px; top: 0; width: 630px; height: 300px;
    background: linear-gradient(90deg, var(--white) 0%, var(--photo-light) 35%, var(--photo-mid) 100%);
  }
  .main-band {
    position: absolute; left: 0; top: 300px; width: 1200px; height: 593px;
    background: var(--navy);
  }
  .nav { position: absolute; top: 311px; left: 0; width: 1200px; height: 59px; }
  .nav-tab {
    position: absolute; top: 0; height: 59px;
    background: var(--tab-blue); color: var(--white);
    font-size: 22px; font-weight: 400;
    display: flex; align-items: center; justify-content: center;
  }
  .nav-tab.is-active {
    height: 69px; background: var(--panel-blue);
    align-items: flex-start; padding-top: 16px; font-weight: 500;
  }
  .nav-gap {
    position: absolute; left: 234px; top: 370px; width: 919px; height: 10px;
    background: var(--gap-blue);
  }
  .content-panel {
    position: absolute; left: 45px; top: 380px; width: 1108px; height: 501px;
    background: var(--panel-blue); color: var(--white);
    font-weight: 300; font-size: 22px; line-height: 28px;
    padding: 78px 40px 0 63px;
  }
  .content-panel p { margin-bottom: 27px; }
  .highlights { list-style: none; margin-bottom: 27px; }
  .highlights li { position: relative; padding-left: 64px; }
  .highlights li::before { content: "·"; position: absolute; left: 0; }
</style>
</head>
<body>
  <header class="site-header">
    <div class="brand">
      <div class="brand-square"></div>
      <div class="brand-name">Marlowcrest<br>Advisory Group</div>
    </div>
    <div class="hero-photo" role="img" aria-label="Photograph of advisors' hands with pens reviewing printed financial charts"></div>
  </header>

  <div class="main-band"></div>

  <nav class="nav">
    <div class="nav-tab is-active" style="left:45px;width:189px;">Home</div>
    <div class="nav-tab" style="left:245px;width:239px;">About Us</div>
    <div class="nav-tab" style="left:494px;width:413px;">Solutions for Diverse Needs</div>
    <div class="nav-tab" style="left:918px;width:235px;">Case Studies</div>
  </nav>
  <div class="nav-gap"></div>

  <main class="content-panel">
    <p>At Marlowcrest Advisory Group, protecting your clients’ families, their businesses, and their lifestyles are at the forefront of all we do.</p>
    <ul class="highlights">
      <li>Unsurpassed service, support, and underwriting</li>
      <li>Licensed to conduct business nationally</li>
      <li>Advising businesses and families for over 50 years</li>
      <li>Independent, objective, and resourceful</li>
    </ul>
    <p>There are many advantages to working with Marlowcrest Advisory Group. We offer the service and attention of a boutique agency, while leveraging the strength of preeminent American and offshore life insurance companies.</p>
    <p>In addition, since we are privately owned we base our actions and recommendations on what is best for our clients without regard to stockholder profit or share price.</p>
  </main>
</body>
</html>
```